Book cover for a book about how to support a friend in grief.

The title of the book is "Quiet Hands on Heavy Days: Standing Beside Someone Across Hard Seasons" by Daniel P. Hartwig. I am a grief counselor and am passionate about educating people on how to better support someone in grief. I'd like the cover to tell a story. Maybe a person in grief and a friend standing near who doesn't know what to say. The image should appeal to all genders. I am open to ANY other ideas for the cover. Grief is a heavy topic but I don't want the cover to feel sad. It should convey hope.

```html
<!DOCTYPE html>
<html lang="en">
<head>
<meta charset="UTF-8">
<title>Quiet Hands on Heavy Days — Daniel P. Hartwig</title>
<link href="https://fonts.googleapis.com/css2?family=Catamaran:wght@700;800&family=Caveat:wght@500&family=Arimo:ital,wght@0,400;1,700&display=swap" rel="stylesheet">
<style>
  :root {
    --sky-top: #1e5066;
    --sky-upper: #2a5f75;
    --sky-mid: #8eb0c1;
    --sky-low: #b7cad3;
    --dusk-glow: #e89a72;
    --horizon: #3a3f49;
    --ground: #121418;
    --ink-light: #ffffff;
  }
  * { margin: 0; padding: 0; box-sizing: border-box; }
  html, body {
    width: 840px;
    height: 1200px;
    overflow: hidden;
    background: var(--ground);
  }
  .cover {
    position: relative;
    width: 840px;
    height: 1200px;
    overflow: hidden;
    color: var(--ink-light);
  }
  .cover-scene {
    position: absolute;
    inset: 0;
    background: linear-gradient(
      to bottom,
      var(--sky-top) 0%,
      var(--sky-upper) 32%,
      var(--sky-mid) 52%,
      var(--sky-low) 72%,
      var(--sky-low) 80%,
      var(--dusk-glow) 86%,
      var(--horizon) 90%,
      var(--ground) 100%
    );
  }
  .title-block {
    position: absolute;
    top: 96px;
    left: 0;
    right: 0;
    text-align: center;
  }
  .title-main {
    font-family: "Catamaran", sans-serif;
    font-weight: 800;
    font-size: 112px;
    line-height: 1;
    letter-spacing: 1px;
  }
  .title-connector {
    font-family: "Caveat", cursive;
    font-weight: 500;
    font-size: 42px;
    line-height: 1;
    letter-spacing: 4px;
    margin: 26px 0 22px;
  }
  .subtitle {
    position: absolute;
    top: 474px;
    left: 0;
    right: 0;
    text-align: center;
    font-family: "Arimo", sans-serif;
    font-style: italic;
    font-weight: 700;
    font-size: 23px;
    letter-spacing: 0.5px;
  }
  .author {
    position: absolute;
    top: 1104px;
    left: 0;
    right: 0;
    text-align: center;
    font-family: "Arimo", sans-serif;
    font-weight: 400;
    font-size: 38px;
    letter-spacing: 4px;
  }
</style>
</head>
<body>
  <main class="cover">
    <div class="cover-scene" role="img" aria-label="Photograph at dusk: two silhouetted figures standing apart on a hilltop, one bent over with head in hands, the other looking up at a fading blue sky above a glowing sunset horizon and a line of trees"></div>

    <h1 class="title-block">
      <span class="title-main" style="display:block">QUIET HANDS</span>
      <span class="title-connector" style="display:block">on</span>
      <span class="title-main" style="display:block">HEAVY DAYS</span>
    </h1>

    <p class="subtitle">Standing Beside Someone Across Hard Seasons</p>

    <p class="author">Daniel P. Hartwig</p>
  </main>
</body>
</html>
```